Develop a PowerPoint template that I can use for my Professional Develoment leadership series.

July 7 – 9:00 AM – Leadership as Core
July 21 – 9:00 AM – Equitable Access
August 4 – 9:00 AM – Academic Pathways
August 18 – 9:00 AM – Robust Student Support
September 1 – 9:00 AM – Connections to Career
September 15 – 9:00 AM – High-Quality and Deep Partnerships

The Leadership series is posted on both the NM and MA websites at http://www.tandelhighprep.com/
http://www.vrqs-lp.com/

I need 2 powerpoints with the same content, just a different look and feel to mirror that of the 2 websites. Please use the color from the two websites and any pictures, etc.

Also, put my company's logo and information in the footer. I am attaching a logo, below is our copyright information:

Copyright © 2020 KB7up™ Bridgeway9Futures™ | All rights reserved

```html
<!DOCTYPE html>
<html lang="en">
<head>
<meta charset="utf-8">
<title>KB7up Leadership Series – Slide Template</title>
<link rel="stylesheet" href="https://fonts.googleapis.com/css2?family=Catamaran:wght@400;500;600&family=Lato:wght@400;700;900&display=swap">
<style>
  :root {
    --page: #eeeeee;
    --slide: #ffffff;
    --orange: #ee6b3b;
    --yellow: #fbcb43;
    --ink: #222222;
    --body: #333333;
    --muted: #6b6b6b;
  }
  * { box-sizing: border-box; margin: 0; padding: 0; }
  html, body { width: 1200px; height: 4000px; overflow: hidden; background: var(--page); }
  body { position: relative; font-family: "Lato", Arial, sans-serif; color: var(--body); }

  .slide { position: absolute; left: 31px; width: 1138px; height: 640px; background: var(--slide); overflow: hidden; }
  .slide--cover { top: 96px; }
  .slide--text { top: 826px; }
  .slide--columns { top: 1555px; }
  .slide--photo { top: 2284px; }
  .slide--quote { top: 3013px; }

  .brand { position: absolute; display: flex; align-items: center; gap: 8px; font-family: "Catamaran", sans-serif; font-weight: 400; color: var(--ink); line-height: 1; }
  .brand__mark { background: var(--orange); }

  /* cover */
  .cover__brand { left: 79px; top: 76px; font-size: 46px; gap: 12px; }
  .cover__brand .brand__mark { width: 38px; height: 38px; }
  .cover__title { position: absolute; left: 79px; top: 262px; font-family: "Catamaran", sans-serif; font-weight: 600; font-size: 36px; line-height: 45px; color: var(--ink); }
  .accent { position: absolute; display: flex; gap: 8px; }
  .accent span { display: block; height: 6px; }
  .accent span:first-child { width: 52px; background: var(--yellow); }
  .accent span:last-child { width: 26px; background: var(--orange); }
  .cover__accent { left: 79px; top: 366px; }
  .cover__date { position: absolute; left: 79px; top: 544px; font-family: "Catamaran", sans-serif; font-size: 20px; color: var(--ink); }
  .cover__date sup { font-size: 11px; }
  .cover__rule { position: absolute; left: 663px; top: 0; width: 6px; height: 640px; background: var(--yellow); }
  .cover__hero { position: absolute; left: 669px; top: 0; width: 469px; height: 640px; background: linear-gradient(160deg, #c9c6b8 0%, #b68c5c 45%, #d9a56a 70%, #8f7a64 100%); }
  .cover__speaker { position: absolute; left: 588px; width: 158px; height: 158px; border: 6px solid var(--orange); background: linear-gradient(150deg, #8d6a4a, #4a3426); }
  .cover__speaker--one { top: 155px; }
  .cover__speaker--two { top: 327px; background: linear-gradient(150deg, #a69c8d, #52617a); }

  /* shared slide parts */
  .slide__title { position: absolute; left: 62px; top: 48px; font-family: "Lato", sans-serif; font-weight: 700; font-size: 31px; letter-spacing: 3px; color: var(--orange); }
  .slide__accent { left: 62px; top: 96px; }
  .slide__subtitle { position: absolute; left: 62px; top: 122px; font-size: 20px; letter-spacing: 2px; color: var(--orange); }
  .body-copy { position: absolute; left: 62px; width: 1015px; font-size: 11.5px; line-height: 15px; letter-spacing: 0.6px; text-align: justify; color: var(--body); }
  .body-copy p + p { margin-top: 20px; }

  .footer__rule { position: absolute; left: 0; top: 598px; width: 970px; height: 3px; background: var(--yellow); }
  .footer__copy { position: absolute; left: 62px; top: 610px; font-size: 8px; font-weight: 900; letter-spacing: 0.5px; color: var(--ink); text-transform: uppercase; }
  .footer__tick { position: absolute; left: 568px; top: 610px; width: 3px; height: 9px; background: var(--orange); }
  .footer__brand { left: 978px; top: 580px; font-size: 30px; }
  .footer__brand .brand__mark { width: 24px; height: 24px; }

  /* columns */
  .columns { position: absolute; left: 62px; top: 354px; width: 1015px; display: grid; grid-template-columns: repeat(3, 1fr); column-gap: 32px; }
  .column__heading { font-size: 20px; font-weight: 700; letter-spacing: 2px; color: var(--ink); }
  .column__rule { width: 42px; height: 3px; margin: 20px 0 16px; background: var(--orange); }
  .column__rule--yellow { background: var(--yellow); }
  .column__text { font-size: 11.5px; line-height: 15px; letter-spacing: 0.6px; text-align: justify; }

  /* photo slide */
  .photo__hero { position: absolute; left: 590px; top: 0; width: 548px; height: 640px; clip-path: polygon(202px 0, 548px 0, 548px 640px, 0 640px); background: linear-gradient(150deg, #efece6 0%, #d7c7b0 40%, #8f7d6c 70%, #3f4148 100%); }
  .photo__copy { position: absolute; left: 62px; font-size: 11.5px; line-height: 15px; letter-spacing: 1px; text-align: justify; color: var(--muted); }
  .photo__brand { color: var(--orange); }

  /* quote */
  .quote__text { position: absolute; left: 109px; top: 110px; width: 430px; font-size: 29px; line-height: 37.5px; letter-spacing: 3px; color: var(--yellow); font-weight: 400; }
  .quote__author { position: absolute; left: 112px; top: 512px; font-size: 25px; font-weight: 700; letter-spacing: 3px; color: var(--ink); }
  .quote__art { position: absolute; left: 0; top: 0; }
</style>
</head>
<body>

<section class="slide slide--cover">
  <div class="brand cover__brand"><span class="brand__mark"></span>KB7up</div>
  <h1 class="cover__title">Leadership as Core<br>to Early College Programs</h1>
  <div class="accent cover__accent"><span></span><span></span></div>
  <p class="cover__date">July 7<sup>th</sup>, 2020</p>
  <div class="cover__rule"></div>
  <div class="cover__hero" role="img" aria-label="Smiling student holding a book outdoors"></div>
  <div class="cover__speaker cover__speaker--one" role="img" aria-label="Portrait of first series presenter"></div>
  <div class="cover__speaker cover__speaker--two" role="img" aria-label="Portrait of second series presenter"></div>
</section>

<section class="slide slide--text">
  <h2 class="slide__title">SLIDE TITLE HERE</h2>
  <div class="accent slide__accent"><span></span><span></span></div>
  <p class="slide__subtitle">SUBTITLE GOES HERE</p>
  <div class="body-copy" style="top:166px">
    <p>Lorem ipsum dolor sit amet, consectetur adipisicing elit, sed do eiusmod tempor incididunt ut labore et dolore magna aliqua. Ut enim ad minim veniam, quis nostrud exercitation ullamco laboris nisi ut aliquip ex ea commodo consequat. Duis aute irure dolor in reprehenderit in voluptate velit esse cillum dolore eu fugiat nulla pariatur.</p>
    <p>Excepteur sint occaecat cupidatat non proident, sunt in culpa qui officia deserunt mollit anim id est laborum. Sed ut perspiciatis unde omnis iste natus error sit voluptatem accusantium doloremque laudantium, totam rem aperiam, eaque ipsa quae ab illo inventore veritatis et quasi architecto beatae vitae dicta sunt explicabo. Nemo enim ipsam voluptatem quia voluptas sit aspernatur aut odit aut fugit, sed quia consequuntur magni dolores eos qui ratione voluptatem sequi nesciunt. Neque porro quisquam est, qui dolorem ipsum quia dolor sit amet, consectetur, adipisci velit, sed quia non numquam eius modi tempora incidunt ut labore et dolore magnam aliquam quaerat voluptatem.</p>
    <p>Lorem ipsum dolor sit amet, consectetur adipisicing elit, sed do eiusmod tempor incididunt ut labore et dolore magna aliqua. Ut enim ad minim veniam, quis nostrud exercitation ullamco laboris nisi ut aliquip ex ea commodo consequat. Duis aute irure dolor in reprehenderit in voluptate velit esse cillum dolore eu fugiat nulla pariatur. Excepteur sint occaecat cupidatat non proident, sunt in culpa qui officia deserunt mollit anim id est laborum. Sed ut perspiciatis unde omnis iste natus error sit voluptatem accusantium doloremque laudantium, totam rem aperiam, eaque ipsa quae ab illo inventore veritatis et quasi architecto beatae vitae dicta sunt explicabo. Nemo enim ipsam voluptatem quia voluptas sit aspernatur aut odit aut fugit, sed quia consequuntur magni dolores eos qui ratione voluptatem sequi nesciunt. Neque porro quisquam est, qui dolorem ipsum quia dolor sit amet, consectetur, adipisci velit, sed quia non numquam eius modi tempora incidunt ut labore et dolore magnam aliquam quaerat voluptatem.</p>
    <p>Inventore veritatis et quasi architecto beatae vitae dicta sunt explicabo. Nemo enim ipsam voluptatem quia voluptas sit aspernatur aut odit aut fugit, sed quia consequuntur magni dolores eos qui ratione voluptatem sequi nesciunt. Neque porro quisquam est, qui dolorem ipsum quia dolor sit amet, consectetur, adipisci velit, sed quia non numquam eius modi tempora incidunt ut labore et dolore magnam aliquam quaerat voluptatem.</p>
  </div>
  <div class="footer__rule"></div>
  <p class="footer__copy">Copyright © 2020 KB7up™ Bridgeway9Futures™ | All rights reserved</p>
  <div class="footer__tick"></div>
  <div class="brand footer__brand"><span class="brand__mark"></span>KB7up</div>
</section>

<section class="slide slide--columns">
  <h2 class="slide__title">SLIDE TITLE HERE</h2>
  <div class="accent slide__accent"><span></span><span></span></div>
  <div class="body-copy" style="top:155px">
    <p>Lorem ipsum dolor sit amet, consectetur adipisicing elit, sed do eiusmod tempor incididunt ut labore et dolore magna aliqua. Ut enim ad minim veniam, quis nostrud exercitation ullamco laboris nisi ut aliquip ex ea commodo consequat. Duis aute irure dolor in reprehenderit in voluptate velit esse cillum dolore eu fugiat nulla pariatur.</p>
    <p>Excepteur sint occaecat cupidatat non proident, sunt in culpa qui officia deserunt mollit anim id est laborum. Sed ut perspiciatis unde omnis iste natus error sit voluptatem accusantium doloremque laudantium, totam rem aperiam, eaque ipsa quae ab illo inventore veritatis et quasi architecto beatae vitae dicta sunt explicabo. Nemo enim ipsam voluptatem quia voluptas sit aspernatur aut odit aut fugit, sed quia consequuntur magni dolores eos qui ratione voluptatem sequi nesciunt. Neque porro quisquam est, qui dolorem ipsum quia dolor sit amet, consectetur, adipisci velit, sed quia non numquam eius modi tempora incidunt ut labore et dolore magnam aliquam quaerat voluptatem.</p>
  </div>
  <div class="columns">
    <div class="column">
      <h3 class="column__heading">SUBTITLE GOES HERE</h3>
      <div class="column__rule"></div>
      <p class="column__text">Lorem ipsum dolor sit amet, consectetur adipisicing elit, sed do eiusmod tempor incididunt ut labore et dolore magna aliqua. Ut enim ad minim veniam, quis nostrud exercitation ullamco laboris nisi ut aliquip ex ea commodo consequat.</p>
    </div>
    <div class="column">
      <h3 class="column__heading">SUBTITLE GOES HERE</h3>
      <div class="column__rule column__rule--yellow"></div>
      <p class="column__text">Lorem ipsum dolor sit amet, consectetur adipisicing elit, sed do eiusmod tempor incididunt ut labore et dolore magna aliqua. Ut enim ad minim veniam, quis nostrud exercitation ullamco laboris nisi ut aliquip ex ea commodo consequat.</p>
    </div>
    <div class="column">
      <h3 class="column__heading">SUBTITLE GOES HERE</h3>
      <div class="column__rule"></div>
      <p class="column__text">Lorem ipsum dolor sit amet, consectetur adipisicing elit, sed do eiusmod tempor incididunt ut labore et dolore magna aliqua. Ut enim ad minim veniam, quis nostrud exercitation ullamco laboris nisi ut aliquip ex ea commodo consequat.</p>
    </div>
  </div>
  <div class="footer__rule"></div>
  <p class="footer__copy">Copyright © 2020 KB7up™ Bridgeway9Futures™ | All rights reserved</p>
  <div class="footer__tick"></div>
  <div class="brand footer__brand"><span class="brand__mark"></span>KB7up</div>
</section>

<section class="slide slide--photo">
  <div class="photo__hero" role="img" aria-label="Adult learners seated together in a bright workshop room"></div>
  <h2 class="slide__title">SLIDE TITLE HERE</h2>
  <div class="accent slide__accent"><span></span><span></span></div>
  <p class="slide__subtitle">SUBTITLE GOES HERE</p>
  <p class="photo__copy" style="top:168px;width:649px">Lorem ipsum dolor sit amet, consectetur adipisicing elit, sed do eiusmod tempor incididunt ut labore et dolore magna aliqua. Ut enim ad minim veniam, quis nostrud exercitation ullamco laboris nisi ut aliquip ex ea commodo consequat. Duis aute irure dolor in reprehenderit in voluptate velit esse cillum dolore eu fugiat nulla pariatur.</p>
  <p class="photo__copy" style="top:253px;width:649px">Excepteur sint occaecat cupidatat non proident, sunt in culpa qui officia deserunt mollit anim id est laborum. Sed ut perspiciatis unde omnis iste natus error sit voluptatem accusantium doloremque laudantium, totam rem aperiam, eaque ipsa qua</p>
  <p class="photo__copy" style="top:321px;width:536px">E ab illo inventore veritatis et quasi architecto beatae vitae dicta sunt explicabo. Nemo enim ipsam voluptatem quia voluptas sit aspernatur aut odit aut fugit, sed quia consequuntur magni dolores eos qui ratione voluptatem sequi nesciunt. Neque porro quisquam est, qui dolorem ipsum quia dolor sit amet, consectetur, adipisci velit, sed quia non numquam eius modi tempora incidunt ut labore et dolore magnam aliquam quaerat voluptatem.</p>
  <p class="photo__copy" style="top:448px;width:536px">Lorem ipsum dolor sit amet, consectetur adipisicing elit, sed do eiusmod tempor incididunt ut labore et dolore magna aliqua. Ut enim ad minim veniam, quis nostrud exercitation ullamco laboris nisi ut aliquip ex ea commodo consequat. Duis</p>
  <div class="footer__rule"></div>
  <p class="footer__copy">Copyright © 2020 KB7up™ Bridgeway9Futures™ | All rights reserved</p>
  <div class="footer__tick"></div>
  <div class="brand footer__brand photo__brand"><span class="brand__mark"></span>KB7up</div>
</section>

<section class="slide slide--quote">
  <blockquote class="quote__text">“Lorem ipsum dolor sit amet, consectetur adip­isicing elit, sed do eius­mod tempor incididunt ut labore et dolore magna aliqua. Ut enim ad minim veniam, quis nostrud exercitation ul­lamco laboris nisi com­modo consequat.”</blockquote>
  <p class="quote__author">John Doe</p>
  <svg class="quote__art" width="1138" height="640" viewBox="0 0 1138 640">
    <defs>
      <linearGradient id="quote-photo-tone" x1="0" y1="0" x2="1" y2="1">
        <stop offset="0" stop-color="#8a6a4c"/>
        <stop offset="0.5" stop-color="#d8c7ae"/>
        <stop offset="1" stop-color="#6d9bb8"/>
      </linearGradient>
    </defs>
    <polygon points="613,88 1075,88 846,523" fill="none" stroke="#ee6b3b" stroke-width="6"/>
    <polygon points="695,135 993,135 844,444" fill="#ee6b3b"/>
    <polygon points="703,140 985,140 844,432" fill="url(#quote-photo-tone)" role="img" aria-label="Student holding books in a library"/>
  </svg>
  <div class="footer__rule"></div>
  <p class="footer__copy">Copyright © 2020 KB7up™ Bridgeway9Futures™ | All rights reserved</p>
  <div class="footer__tick"></div>
  <div class="brand footer__brand"><span class="brand__mark"></span>KB7up</div>
</section>

</body>
</html>
```